" É uma pequena fábrica com injetoras plásticas, e a produção poderá ser a mais variada possível. Podemos, por exemplo, criar desde utensílios plásticos (cabide, potes, baldes), brinquedos e, até mesmo, peças para indústrias. Temos também a parte de reciclagem, onde tratamos o plástico desde o lixo até a produção destes itens. No meu ponto de vista deve ser algo genérico, que demonstre criação, inovação, transformação, visão de futuro. "

```html
<!DOCTYPE html>
<html lang="pt-BR">
<head>
<meta charset="UTF-8">
<title>Cartão de visita – Vortan</title>
<link rel="stylesheet" href="https://fonts.googleapis.com/css2?family=Montserrat:wght@400;600;700;800&display=swap">
<style>
  :root{
    --navy:#142a4e;
    --navy-deep:#0f2142;
    --orange:#f37a1f;
    --paper:#ffffff;
    --ink:#2b2f36;
    --muted:#6b7078;
    --stage:#e9eaec;
    --icon:#3a3f47;
  }
  *{box-sizing:border-box;margin:0;padding:0}
  html,body{width:1200px;height:1200px;overflow:hidden}
  body{background:var(--stage);font-family:"Montserrat",sans-serif;position:relative}
  .card{position:absolute;left:220px;width:760px;height:422px;border-radius:4px;overflow:hidden;box-shadow:0 10px 30px rgba(0,0,0,.12)}
  .card--front{top:110px;background:var(--navy)}
  .card--back{top:660px;background:var(--paper)}
  .card__band{position:absolute;left:0;bottom:0;width:100%;height:70px}
  .brand{position:absolute;display:flex;flex-direction:column;align-items:flex-start}
  .brand__name{font-weight:800;letter-spacing:.04em;line-height:1}
  .brand__tag{font-weight:400;letter-spacing:.32em;text-transform:uppercase}
  .card--front .brand{left:232px;top:140px}
  .card--front .brand__name{color:#fff;font-size:88px}
  .card--front .brand__tag{color:#fff;font-size:22px;margin-top:8px}
  .card--back .brand{right:58px;bottom:98px}
  .card--back .brand__name{color:var(--navy);font-size:58px}
  .card--back .brand__tag{color:var(--navy);font-size:14px;margin-top:6px}
  .contact{position:absolute;left:46px;top:46px;list-style:none}
  .contact__item{display:flex;align-items:center;gap:14px;color:var(--muted);font-size:15px;margin-bottom:16px}
  .contact__item svg{flex:none;width:22px;height:22px}
  .contact__item--name{color:var(--ink);font-weight:700;font-size:24px;margin-bottom:22px}
  .contact__item--name svg{width:26px;height:26px}
  .contact__address{line-height:1.5;font-size:14px}
</style>
</head>
<body>
  <section class="card card--front" aria-label="Frente do cartão">
    <div class="brand">
      <span class="brand__name">VORTAN</span>
      <span class="brand__tag">Injeção Plástica</span>
    </div>
    <svg class="card__band" viewBox="0 0 760 70" preserveAspectRatio="none" aria-hidden="true">
      <path d="M300 70 L380 52 L760 30 L760 70 Z" fill="var(--navy-deep)"/>
      <path d="M330 70 L400 58 L760 46 L760 70 Z" fill="var(--orange)"/>
    </svg>
  </section>

  <section class="card card--back" aria-label="Verso do cartão">
    <ul class="contact">
      <li class="contact__item contact__item--name">
        <svg viewBox="0 0 24 24"><circle cx="12" cy="12" r="12" fill="var(--icon)"/><circle cx="12" cy="9" r="4" fill="#fff"/><path d="M5 19c1.5-4 12.5-4 14 0" fill="#fff"/></svg>
        Nome Sobrenome
      </li>
      <li class="contact__item">
        <svg viewBox="0 0 24 24"><circle cx="12" cy="12" r="12" fill="var(--icon)"/><path d="M8 6h3l1 3-2 1.2a8 8 0 0 0 3.8 3.8L15 12l3 1v3c-6 .5-10.5-4-10-10z" fill="#fff"/></svg>
        (xx) xxxxx-xxxxx
      </li>
      <li class="contact__item">
        <svg viewBox="0 0 24 24"><circle cx="12" cy="12" r="12" fill="var(--icon)"/><rect x="6" y="8" width="12" height="8" rx="1" fill="#fff"/><path d="M6.5 8.5 12 12.5l5.5-4" stroke="var(--icon)" stroke-width="1.2" fill="none"/></svg>
        contato@empresa.com.br
      </li>
      <li class="contact__item">
        <svg viewBox="0 0 24 24"><circle cx="12" cy="12" r="12" fill="var(--icon)"/><path d="M12 5a4.5 4.5 0 0 0-4.5 4.5C7.5 13 12 19 12 19s4.5-6 4.5-9.5A4.5 4.5 0 0 0 12 5z" fill="#fff"/><circle cx="12" cy="9.5" r="1.6" fill="var(--icon)"/></svg>
        <span class="contact__address">Rua Exemplo, nº 000, 1º andar,<br>Bairro, CEP 00000-000, Cidade/UF</span>
      </li>
    </ul>
    <div class="brand">
      <span class="brand__name">VORTAN</span>
      <span class="brand__tag">Injeção Plástica</span>
    </div>
    <svg class="card__band" viewBox="0 0 760 70" preserveAspectRatio="none" aria-hidden="true">
      <path d="M0 40 L300 40 L370 62 L760 62 L760 64 L368 64 L298 43 L0 43 Z" fill="#c9ccd1"/>
      <path d="M0 50 L290 50 L350 70 L0 70 Z" fill="var(--orange)"/>
    </svg>
  </section>
</body>
</html>
```